Red heron

Retail sales of clothing related to outdoor sports, exercise, activities and socialization
Updates

please use more clothing accessories
golf beach sports running yoga pilates gym etc rather than equipment for now

please use logo designed

hello

can I get a link / page to
RED HERON MENTAL HEALTH GROUP CIC
promoting outdoor activities, exercis, outdoors and socialization to help with mental health issues
Courage strength and loyalty

use the social media image 2 wolves howling to the moon

Please

This is a non profit charity
proceeds from red heron LLC sales will be donated to this non profit company to help those in UK with mental health issues

Target Market(s)

All

Industry/Entity Type

Retail e-commerce

Coding

Coded - Design and coding required

Number of Pages Required

5+ page

Font styles to use
Other font styles liked:
• To fit with red heron logo design

Colors
0054AA
0677BA
7BADD7
CADEEF
E8F1F8

Requirements
Must have
• Ability to accept payments, link to a not for profit business to be supplied for donations of proceeds of sale, ability to link to activities
Nice to have
• Ai associated customers service, email, blog, WhatsApp, links to social media

```html
<!DOCTYPE html>
<html lang="en">
<head>
<meta charset="utf-8">
<title>Red heron — Retail sales of outdoor sports and socialization</title>
<link href="https://fonts.googleapis.com/css2?family=Poppins:wght@300;400;500;600;700&family=Marcellus&display=swap" rel="stylesheet">
<style>
:root{
  --navy:#0b2e97;
  --blue:#0a57d6;
  --blue-deep:#0054aa;
  --blue-mid:#0677ba;
  --sky:#7badd7;
  --mist:#cadeef;
  --ice:#e8f1f8;
  --ink:#333a4a;
  --grey:#6d7180;
  --white:#ffffff;
}
*{margin:0;padding:0;box-sizing:border-box}
html,body{width:1200px;height:4494px;overflow:hidden}
body{position:relative;font-family:'Poppins',sans-serif;color:var(--ink);background:var(--white)}
.abs{position:absolute}
a{color:inherit;text-decoration:none}

/* Header & hero */
.hero{left:0;top:0;width:1200px;height:656px;background:linear-gradient(160deg,#5b7fb8 0%,#a9bfdc 30%,#e6edf6 55%,#8ea7cc 75%,#3e5f98 100%)}
.brand{left:54px;top:22px;display:flex;align-items:center;gap:10px;color:var(--white);font-weight:600;font-size:24px;line-height:1}
.brand-dot{width:44px;height:44px;border-radius:50%;border:2px solid var(--white)}
.nav{left:256px;top:40px;display:flex;gap:33px;font-size:13px;font-weight:600;color:var(--white)}
.cart{left:921px;top:35px}
.donate-btn{left:963px;top:25px;width:186px;height:48px;border-radius:24px;background:var(--blue);color:var(--white);font-size:14px;font-weight:600;display:flex;align-items:center;justify-content:center}
.hero-title{left:640px;top:185px;font-size:74px;font-weight:700;color:var(--white);line-height:1;letter-spacing:1px}
.hero-sub{left:640px;top:286px;font-size:30px;font-weight:300;color:var(--white);line-height:41px;width:480px}
.btn-blue{background:var(--blue);color:var(--white);border-radius:28px;font-weight:600;font-size:16px;display:flex;align-items:center;justify-content:center}
.hero-btn{left:644px;top:391px;width:150px;height:52px}

/* Activities */
.sec-title{left:0;width:1200px;text-align:center;color:var(--navy);font-weight:600;font-size:40px;line-height:1}
.act-title{top:755px}
.act-intro{left:170px;top:816px;width:860px;text-align:center;font-size:15px;line-height:24px;color:var(--ink)}
.tile{width:286px;height:248px;display:flex;align-items:center;justify-content:center;color:var(--white);font-weight:700;font-size:19px;letter-spacing:.3px}
.t1{background:linear-gradient(160deg,#6c8fc0,#b24a3a 60%,#6a6f55)}
.t2{background:linear-gradient(170deg,#7a6a52,#4d4a3e 50%,#8e8b7f)}
.t3{background:linear-gradient(160deg,#4f7f5a,#6aa2a5 50%,#c2a331)}
.t4{background:linear-gradient(170deg,#9db8d4,#8c6b56 50%,#4a6b8c)}
.t5{background:linear-gradient(160deg,#3f6b32,#a8773c 55%,#6b4a2e)}
.t6{background:linear-gradient(160deg,#4b4e55,#b5b9c1 55%,#e7e0d8)}

/* About */
.about{left:0;top:1547px;width:1200px;height:596px;background:linear-gradient(120deg,#3e6dc0 0%,#1f5dd1 45%,#0a57d6 100%)}
.about-rule{left:0;top:2139px;width:865px;height:4px;background:var(--navy)}
.about-mark{left:125px;top:1665px;width:285px;height:370px;display:flex;align-items:center;justify-content:center}
.about-mark .ring{width:260px;height:260px;border-radius:50%;border:4px solid var(--white);display:flex;align-items:center;justify-content:center;color:var(--white);font-weight:600;font-size:30px}
.about-title{left:492px;top:1672px;font-size:40px;font-weight:700;color:var(--white);line-height:1}
.about-text{left:492px;top:1742px;width:572px;font-size:15px;line-height:23.2px;color:var(--white)}
.about-btn{left:492px;top:1985px;width:152px;height:56px;border:2px solid var(--white);border-radius:28px;color:var(--white);font-weight:600;font-size:16px;display:flex;align-items:center;justify-content:center}

/* Products */
.sales-title{top:2228px}
.card{top:2332px;width:293px;height:397px;background:var(--white);box-shadow:0 2px 14px rgba(0,0,0,.08);text-align:center}
.card.round{top:2320px;height:435px;border-radius:140px}
.card .pic{margin:26px auto 0;width:210px;height:190px;border-radius:6px}
.card.round .pic{margin-top:38px}
.card h3{margin-top:40px;font-size:22px;font-weight:600;color:var(--blue)}
.card p{margin:10px auto 0;width:250px;font-size:14.5px;line-height:20px;color:var(--grey)}
.p1{background:linear-gradient(90deg,#f2c33c,#e25a8c,#6b5ad1,#2fa6d8)}
.p2{background:linear-gradient(180deg,#f4f4f4,#bfc2c6 50%,#6a6d72)}
.p3{background:linear-gradient(160deg,#e33a3a,#b7b7b7 60%,#4a86b8)}
.arrow{width:54px;height:54px}
.divider{left:127px;width:946px;height:2px;background:var(--blue)}

/* Blog */
.blog-title{left:0;top:2940px;width:1200px;text-align:center;font-family:'Marcellus',serif;font-size:46px;color:var(--navy);line-height:1}
.blog-title span{font-size:36px}
.post{top:3048px;width:223px}
.post .pic{width:223px;height:295px}
.post .pic.oval{border-radius:50%}
.post h3{margin-top:36px;font-size:21px;line-height:25px;font-weight:600;color:var(--blue)}
.post p{margin-top:20px;font-size:14px;line-height:20.5px;color:var(--grey)}
.b1{background:linear-gradient(180deg,#f0c064,#d68a2e 50%,#3b3a1e)}
.b2{background:linear-gradient(180deg,#3b6ec4,#9fbce0 50%,#f2f5fa)}
.b3{background:linear-gradient(160deg,#c6cfd8,#3e9aa8 50%,#7a6a5e)}
.b4{background:linear-gradient(180deg,#dfe8ef,#2f8ba6 55%,#e0c23a)}
.view-btn{left:525px;top:3601px;width:150px;height:56px}

/* Newsletter & footer */
.footer{left:0;top:3887px;width:1200px;height:607px;background:var(--blue)}
.news-pill{left:127px;top:3818px;width:946px;height:181px;border-radius:90px;background:var(--navy)}
.news-title{left:188px;top:3892px;font-size:30px;font-weight:700;color:var(--white)}
.news-label{left:530px;top:3895px;font-size:13px;color:var(--white)}
.news-line{left:530px;top:3922px;width:311px;height:1px;background:var(--white)}
.news-sign{left:909px;top:3902px;font-size:17px;font-weight:600;color:var(--white)}
.foot-brand{left:127px;top:4079px;display:flex;align-items:center;gap:10px;color:var(--white);font-weight:600;font-size:24px}
.foot-about{left:127px;top:4164px;width:210px;font-size:14px;line-height:25px;color:var(--white)}
.col-head{font-size:19px;font-weight:600;color:var(--white)}
.col-links{list-style:none;font-size:14px;line-height:31.7px;color:var(--white)}
.field{left:773px;top:4119px;width:300px;height:53px;border-radius:27px;background:var(--white);font-size:12px;font-weight:600;color:var(--ink);padding:19px 0 0 20px}
.field-btn{left:773px;top:4182px;width:300px;height:53px;border-radius:27px;background:var(--navy);color:var(--white);font-weight:600;font-size:17px;display:flex;align-items:center;justify-content:center}
.social{width:29px;height:29px;border-radius:50%;background:var(--navy)}
.foot-rule{left:127px;top:4370px;width:946px;height:2px;background:var(--white)}
.copy{left:127px;top:4420px;font-size:15px;color:var(--white)}
.pay{top:4412px;width:58px;height:42px;background:var(--white);border-radius:3px;display:flex;align-items:center;justify-content:center;font-size:11px;font-weight:600;color:var(--navy)}
</style>
</head>
<body>

<!-- Hero -->
<div class="abs hero" role="img" aria-label="Skiers descending a snowy mountain slope among frosted trees"></div>
<div class="abs brand"><span class="brand-dot"></span>RED HERON</div>
<nav class="abs nav"><a>HOME</a><a>ABOUT</a><a>PRODUCTS</a><a>RETAIL BUYERS</a><a>BLOG</a><a>ACTIVITIES</a><a>CONTACT</a></nav>
<svg class="abs cart" width="22" height="26" viewBox="0 0 22 26" fill="none" stroke="#fff" stroke-width="2"><rect x="2" y="7" width="18" height="17" rx="2"/><path d="M7 10V6a4 4 0 0 1 8 0v4"/></svg>
<a class="abs donate-btn">DONATED PER SALE</a>
<h1 class="abs hero-title">RED HERON</h1>
<p class="abs hero-sub">Retail sales of outdoor sports and socialization.</p>
<a class="abs btn-blue hero-btn">SHOP NOW</a>

<!-- Activities -->
<h2 class="abs sec-title act-title">Activities-Focused with Retail Buyers</h2>
<p class="abs act-intro">Lorem ipsum dolor sit amet, consectetur adipiscing elit, sed do eiusmod tempor incididunt ut labore et dolore magna aliis ipsum suspendisse ultrices gravid commodo viverra maecenas accumsan lacilisis.</p>
<div class="abs tile t1" style="left:127px;top:895px" role="img" aria-label="Hikers with backpacks facing snowy peaks">CAMP+HIKE</div>
<div class="abs tile t2" style="left:457px;top:895px" role="img" aria-label="Cyclists riding along a mountain road">RUN + CYCLE</div>
<div class="abs tile t3" style="left:787px;top:895px" role="img" aria-label="Kayakers paddling on a tropical lake">WATER SPORTS</div>
<div class="abs tile t4" style="left:127px;top:1174px" role="img" aria-label="Climbers helping each other up a rock face">CLIMB</div>
<div class="abs tile t5" style="left:457px;top:1174px" role="img" aria-label="Friends sitting together on a picnic blanket">SOCIALIZATION</div>
<div class="abs tile t6" style="left:787px;top:1174px" role="img" aria-label="Shop assistant with a tablet in a clothing store">RETAIL SERVICES</div>

<!-- About -->
<div class="abs about" role="img" aria-label="Skier on a snowy slope under a blue overlay"></div>
<div class="abs about-rule"></div>
<div class="abs about-mark"><div class="ring">RED HERON</div></div>
<h2 class="abs about-title">ABOUT RED HERON</h2>
<p class="abs about-text">Sed ut perspiciatis unde omnis iste natus error sit voluptatem accusa ntium doloremque laudantiumotamrem aperiam, eaque ipsa quae ab illo inventore veritatis et quasi architecto beatae vitae dicta sunt explicabo. Nemo enim ipsam voluptatem quia voluptas sit aspernatur aut odit autfu gitsed quia consequuntur magni dolores eos qui ratione voluptatem sequi nesciunt. Neque porro quisquam eui dolorem ipsum quia dolor sit amet, consectetur, adipisci velit, sed quia non numquamem vel eum iure reprhe nderit qui in ea voluptate velit esse quam nihil molestiae consequatuvel illum qui dolorem eum fugiat quo volu.</p>
<a class="abs about-btn">SHOP NOW</a>

<!-- Latest sales -->
<h2 class="abs sec-title sales-title">LATEST SALES OF GOODS</h2>
<svg class="abs arrow" style="left:34px;top:2490px" viewBox="0 0 54 54" fill="none" stroke="#111" stroke-width="2.5"><circle cx="27" cy="27" r="25"/><path d="M31 17l-10 10 10 10"/></svg>
<svg class="abs arrow" style="left:1098px;top:2490px" viewBox="0 0 54 54" fill="none" stroke="#111" stroke-width="2.5"><circle cx="27" cy="27" r="25"/><path d="M23 17l10 10-10 10"/></svg>
<article class="abs card" style="left:127px"><div class="pic p1" role="img" aria-label="Colourful longboard skateboard"></div><h3>Product Name</h3><p>Lorem ipsum dolor sit amet, consectetur adipiscing elit, sed do eiusmod tempor incid</p></article>
<article class="abs card" style="left:453px"><div class="pic p2" role="img" aria-label="Electric kick scooter"></div><h3>Product Name</h3><p>Lorem ipsum dolor sit amet, consectetur adipiscing elit, sed do eiusmod tempor incid</p></article>
<article class="abs card round" style="left:780px"><div class="pic p3" role="img" aria-label="Red hiking backpack with boots and sleeping mat"></div><h3>Product Name</h3><p>Lorem ipsum dolor sit amet, consectetur adipiscing elit, sed do eiusmod tempor incid</p></article>
<div class="abs divider" style="top:2866px"></div>

<!-- Blog -->
<h2 class="abs blog-title">L<span>ATEST</span> B<span>LOG</span></h2>
<article class="abs post" style="left:127px"><div class="pic b1" role="img" aria-label="Football on grass at sunset with a player behind"></div><h3>Lorem ipsum dolor sit ame consec.</h3><p>Lorem ipsum dolor sit amet, consectetur adipiscing elit, sed do eiusmod tempor inc ididunt ut labore et dolore magna aliqua.</p></article>
<article class="abs post" style="left:368px"><div class="pic oval b2" role="img" aria-label="Skis and poles standing in snow"></div><h3>Lorem ipsum dolor sit ame consec.</h3><p>Lorem ipsum dolor sit amet, consectetur adipiscing elit, sed do eiusmod tempor inc ididunt ut labore et dolore magna aliqua.</p></article>
<article class="abs post" style="left:609px"><div class="pic b3" role="img" aria-label="Climbers giving a high five in the mountains"></div><h3>Lorem ipsum dolor sit ame consec.</h3><p>Lorem ipsum dolor sit amet, consectetur adipiscing elit, sed do eiusmod tempor inc ididunt ut labore et dolore magna aliqua.</p></article>
<article class="abs post" style="left:849px"><div class="pic b4" role="img" aria-label="Kayaker paddling a yellow kayak"></div><h3>Lorem ipsum dolor sit ame consec.</h3><p>Lorem ipsum dolor sit amet, consectetur adipiscing elit, sed do eiusmod tempor inc ididunt ut labore et dolore magna aliqua.</p></article>
<a class="abs btn-blue view-btn">VIEW ALL</a>
<div class="abs divider" style="top:3722px"></div>

<!-- Newsletter & footer -->
<div class="abs footer"></div>
<div class="abs news-pill"></div>
<h2 class="abs news-title">NEWSLETTER SIGNUP</h2>
<span class="abs news-label">Email:</span>
<div class="abs news-line"></div>
<a class="abs news-sign">SIGN UP</a>

<div class="abs foot-brand"><span class="brand-dot"></span>RED HERON</div>
<p class="abs foot-about">Lorem ipsum dolor sit am et, consectetur adipiscing elit, sed do eiusmod tem por incididunt ut labore et dolore magna aliqua.</p>

<div class="abs" style="left:371px;top:4064px"><h4 class="col-head">Customers Service</h4></div>
<ul class="abs col-links" style="left:375px;top:4108px"><li>Support</li><li>Track My Order</li><li>Return Policy</li><li>Flagship Store</li><li>Store Locator</li><li>Wholesale</li><li>Corporate Gifting</li></ul>
<div class="abs" style="left:635px;top:4064px"><h4 class="col-head">Links</h4></div>
<ul class="abs col-links" style="left:638px;top:4108px"><li>Home</li><li>About</li><li>Products</li><li>Retail Buyers</li><li>Blog</li><li>Activities</li><li>Contact</li></ul>
<div class="abs" style="left:771px;top:4064px"><h4 class="col-head">Newsletter</h4></div>
<div class="abs field">Email:</div>
<a class="abs field-btn">SIGN UP</a>
<span class="abs social" style="left:785px;top:4260px" aria-label="Social link"></span>
<span class="abs social" style="left:823px;top:4260px" aria-label="Social link"></span>
<span class="abs social" style="left:861px;top:4260px" aria-label="Social link"></span>
<span class="abs social" style="left:899px;top:4260px" aria-label="Social link"></span>
<span class="abs social" style="left:937px;top:4260px" aria-label="Social link"></span>
<span class="abs social" style="left:785px;top:4294px" aria-label="Social link"></span>

<div class="abs foot-rule"></div>
<p class="abs copy">Copyright© 2025 Red heron. All Rights Reserved</p>
<span class="abs pay" style="left:698px">Orbit</span>
<span class="abs pay" style="left:762px">Tally</span>
<span class="abs pay" style="left:826px">Nimbus</span>
<span class="abs pay" style="left:890px">Kestrel</span>
<span class="abs pay" style="left:953px">Vela</span>
<span class="abs pay" style="left:1015px">Pebble</span>

</body>
</html>
```